International Freight Forwarder need a business card

We need a logo design for a freight forwarding company . We are active in Sea Transportation, Truck transportation, and Air Transportation, The design should be have normal dimensions of a card and should not have cuts and holes in its design (printed design is required - lamination accepted)

The said company is agent and sales representative of 2 other Shipping companies (whose logos, name, and website should also be mentioned on the card)

Industry/Entity Type

Logistics

Contact Information for Business Card

Address is "No.7, 2nd Sarv Baghestan-e-Nouri, Tehran, IR
Tel number is +98 21 66394512
Fax number is +98 21 66395830
E-Mail address is info@roshanbarsaz.com
Website is www.roshanbarsaz.com

Open Layer Logos attached as well

Colors
33a6d7
0292cd
0255a3
3276b5
85abd2
85cae6
cee9f5
d5e2ee
ffffff

Requirements
Must have
• Main logo of Roshan Barsaz
• Logo of TQM Shipping Line
• London, United Kingdom
• tqmline.com
• Logo of Calm Reef Shipping
• Dubai, United Arab Emirates
• crsuae.com
• We require OPEN layer file to be submitted to us upon project selection.
Should not have
• Weird Designs such as cuts to the shape or holes in design.

```html
<!DOCTYPE html>
<html lang="en">
<head>
<meta charset="utf-8">
<title>Roshan Barsaz – Business Card</title>
<link rel="stylesheet" href="https://fonts.googleapis.com/css2?family=Lato:wght@400;700;900&display=swap">
<style>
  :root {
    --page: #eef0f2;
    --card-white: #ffffff;
    --navy: #1d2c6b;
    --brand-blue: #0255a3;
    --brand-mid: #3276b5;
    --brand-light: #85abd2;
    --text-dark: #1f2a4d;
    --text-grey: #5a6170;
    --rule-grey: #c9ccd2;
    --on-navy: #ffffff;
    --on-navy-soft: #c7cfe6;
  }
  * { box-sizing: border-box; margin: 0; padding: 0; }
  html, body { width: 1200px; height: 815px; overflow: hidden; }
  body {
    background: var(--page);
    font-family: "Lato", Arial, sans-serif;
    display: flex;
    flex-direction: column;
    align-items: center;
    justify-content: center;
    gap: 40px;
  }
  .card {
    width: 612px;
    height: 350px;
    display: grid;
    grid-template-columns: 1fr 1px 1fr;
    align-items: center;
    box-shadow: 0 6px 18px rgba(20, 30, 60, .12);
  }
  .card--front { background: var(--card-white); }
  .card--back  { background: var(--navy); }

  .card__divider { height: 56%; background: var(--rule-grey); }
  .card--back .card__divider { background: rgba(255,255,255,.28); }

  /* Front: brand block */
  .brand { display: flex; flex-direction: column; align-items: center; gap: 14px; }
  .brand__mark { width: 92px; height: 92px; border-radius: 50%; border: 3px solid var(--brand-light); }
  .brand__name {
    color: var(--brand-blue);
    font-weight: 700;
    font-size: 15px;
    line-height: 1.3;
    text-align: center;
  }

  /* Front: contact block */
  .contact { padding-left: 34px; }
  .contact__name { color: var(--text-dark); font-weight: 900; font-size: 21px; letter-spacing: .5px; }
  .contact__role { color: var(--text-grey); font-size: 12px; margin: 2px 0 18px; }
  .contact__list { list-style: none; display: flex; flex-direction: column; gap: 7px; }
  .contact__item { display: flex; align-items: flex-start; gap: 10px; color: var(--text-dark); font-size: 12px; line-height: 1.35; }
  .contact__icon { width: 16px; height: 14px; flex: none; fill: var(--brand-mid); }

  /* Back: partner blocks */
  .partner { display: flex; flex-direction: column; align-items: center; text-align: center; color: var(--on-navy); }
  .partner__mark { width: 74px; height: 74px; border-radius: 50%; margin-bottom: 14px; }
  .partner__mark--solid { background: var(--on-navy); }
  .partner__mark--ring { border: 2px solid var(--on-navy); }
  .partner__name { font-weight: 700; font-size: 14px; letter-spacing: 2px; text-transform: uppercase; line-height: 1.3; }
  .partner__place, .partner__web {
    color: var(--on-navy-soft);
    font-size: 10.5px;
    letter-spacing: 1.5px;
    text-transform: uppercase;
  }
  .partner__place { margin-top: 12px; }
  .partner__web { margin-top: 3px; }
</style>
</head>
<body>

  <section class="card card--front" aria-label="Business card front">
    <div class="brand">
      <div class="brand__mark"></div>
      <p class="brand__name">Roshan Barsaz<br>International<br>Transport.Co LLc</p>
    </div>
    <div class="card__divider"></div>
    <div class="contact">
      <h1 class="contact__name">DANIEL HARWOOD</h1>
      <p class="contact__role">Registrar</p>
      <ul class="contact__list">
        <li class="contact__item">
          <svg class="contact__icon" viewBox="0 0 16 14"><path d="M3 1h3l1 3-2 1.5a8 8 0 0 0 4 4L10.5 8l3 1v3a1.5 1.5 0 0 1-1.5 1.5C6 13.5 1.5 9 1.5 2.5A1.5 1.5 0 0 1 3 1z"/></svg>
          <span>+98 21 66394512</span>
        </li>
        <li class="contact__item">
          <svg class="contact__icon" viewBox="0 0 16 14"><rect x="4" y="1" width="8" height="4"/><rect x="1" y="5" width="14" height="6" rx="1"/><rect x="4" y="9" width="8" height="4" fill="#fff" stroke="currentColor"/></svg>
          <span>+98 21 66395830</span>
        </li>
        <li class="contact__item">
          <svg class="contact__icon" viewBox="0 0 16 14"><path d="M1 2h14v10H1z"/><path d="M1 2l7 6 7-6" fill="none" stroke="#fff" stroke-width="1.4"/></svg>
          <span>info@roshanbarsaz.com</span>
        </li>
        <li class="contact__item">
          <svg class="contact__icon" viewBox="0 0 16 14"><rect x="1" y="1" width="14" height="12" rx="1.5"/><rect x="2.5" y="4" width="11" height="7.5" fill="#fff"/></svg>
          <span>www.roshanbarsaz.com</span>
        </li>
        <li class="contact__item">
          <svg class="contact__icon" viewBox="0 0 16 14"><path d="M8 0a4.5 4.5 0 0 1 4.5 4.5C12.5 8 8 14 8 14S3.5 8 3.5 4.5A4.5 4.5 0 0 1 8 0z"/><circle cx="8" cy="4.5" r="1.7" fill="#fff"/></svg>
          <span>No.7, 2nd Sarv Baghestan-e-Nouri,<br>Tehran, IR</span>
        </li>
      </ul>
    </div>
  </section>

  <section class="card card--back" aria-label="Business card back">
    <div class="partner">
      <div class="partner__mark partner__mark--solid"></div>
      <p class="partner__name">Calm Reef<br>Shipping LLC</p>
      <p class="partner__place">Dubai, United Arab Emirates</p>
      <p class="partner__web">www.crsuae.com</p>
    </div>
    <div class="card__divider"></div>
    <div class="partner">
      <div class="partner__mark partner__mark--ring"></div>
      <p class="partner__name">TQM<br>Shipping Line Ltd</p>
      <p class="partner__place">London United Kingdom</p>
      <p class="partner__web">www.tqmline.com</p>
    </div>
  </section>

</body>
</html>
```